Packaging design for handmade soap

We are looking for a packaging design for a brand new product line: handmade soaps, called VELMO

We are looking for a design of an outer box together with the logo. We need the design for a 90x65x30mm box (see attached). We trying to get a high-end product preferable with vintage elements (but we don't want a shiny box, it will be finished with matte lacque, however logo or other certain elements could be shiny).

The design should reflect the fact that we have a handmade, all natural soap.

I uploaded a couple of packaging examples I like.

UPDATE 1: It also should have a title, which describes the product more accurate, like "Natural Soap with Seabuckthorn and Olive oil"

UPDATE 2: I would remove the expression "high-end" from the description if high end would mean a lot of flowers in the background. I would like if you would insist about the ideea of "natural" in your works

UPDATE 3: Prefered colors green and brown (which brings the ideea of nature, natural)

Target Market(s)

Women 20-45 years with above average income

Industry/Entity Type

Cosmetics

Font styles to use
Serif

Colors
9bcb3c
acd036
cadf82
f78f20
ffc214
f37122
fbed22
fece3e
faa54b

Requirements
Must have
• A literal representation of the brand VELMO (we don't have a logo for it)

```html
<!DOCTYPE html>
<html lang="en">
<head>
<meta charset="utf-8">
<title>VELMO Naturals – Bar Soap Box Front</title>
<link rel="stylesheet" href="https://fonts.googleapis.com/css2?family=Marcellus&family=Marcellus+SC&family=Oswald:wght@400&family=Questrial&display=swap">
<style>
  :root {
    --page: #f4f4f2;
    --paper: #ffffff;
    --leaf-green: #8dbd2b;
    --leaf-light: #cadf82;
    --petal-grey: #b9b9b9;
    --ink-grey: #8a8a8a;
    --band-text: #ffffff;
  }
  html, body {
    margin: 0;
    width: 1200px;
    height: 686px;
    overflow: hidden;
    background: var(--page);
  }
  .canvas {
    position: relative;
    width: 1200px;
    height: 686px;
  }
  .box-front {
    position: absolute;
    left: 250px;
    top: 90px;
    width: 700px;
    height: 506px;
    background: var(--paper);
    box-shadow: 0 2px 14px rgba(0, 0, 0, 0.08);
    overflow: hidden;
  }
  .floral-band {
    position: absolute;
    left: 0;
    top: 0;
    width: 100%;
    height: 150px;
    background: linear-gradient(100deg, var(--leaf-light) 0%, #dcdcdc 30%, var(--leaf-light) 55%, #d4d4d4 80%, var(--leaf-light) 100%);
  }
  .label-copy {
    position: absolute;
    left: 0;
    top: 150px;
    width: 100%;
    text-align: center;
  }
  .brand-tagline {
    margin: 0;
    padding-top: 14px;
    font-family: "Questrial", sans-serif;
    font-size: 17px;
    letter-spacing: 5px;
    color: var(--leaf-green);
  }
  .brand-name {
    margin: 0;
    font-family: "Marcellus", serif;
    font-size: 86px;
    line-height: 1;
    letter-spacing: 6px;
    color: var(--leaf-green);
  }
  .product-title {
    margin: 14px 0 0;
    font-family: "Marcellus SC", serif;
    font-size: 26px;
    color: var(--leaf-green);
  }
  .product-subtitle {
    margin: 2px 0 0;
    font-family: "Questrial", sans-serif;
    font-size: 20px;
    color: var(--leaf-green);
  }
  .product-band {
    margin-top: 14px;
    height: 46px;
    background: var(--leaf-green);
    display: flex;
    align-items: center;
    justify-content: center;
    font-family: "Oswald", sans-serif;
    font-size: 30px;
    letter-spacing: 2px;
    color: var(--band-text);
  }
  .net-weight {
    margin: 8px 0 0;
    font-family: "Marcellus", serif;
    font-size: 17px;
    color: var(--leaf-green);
  }
</style>
</head>
<body>
  <main class="canvas">
    <section class="box-front">
      <div class="floral-band" role="img" aria-label="Decorative pattern of green and grey flowers and leaves"></div>
      <div class="label-copy">
        <p class="brand-tagline">NATURALS</p>
        <h1 class="brand-name">VELMO</h1>
        <p class="product-title">Natural Soap</p>
        <p class="product-subtitle">with Seabuckthorn and Olive oil</p>
        <div class="product-band">BAR SOAP</div>
        <p class="net-weight">4 oz.</p>
      </div>
    </section>
  </main>
</body>
</html>
```